Business Card Design

We need a new business card design for a company based in Brennick Falls, CO. We provide business consulting services in the information technology / services space. We like variations of the color blue, aqua, black, light tan, and white. Would like "cool" tones. The design should clearly communicate professionalism. Think outside the box - we don't want something "typical". Our company name is "Vantrell Advisory, LLC".
Updates

Thank you all for your submissions. We have seen some very creative and inspired designs. We have made a decision and will be moving forward with that design. Appreciate all of the hard work.

Industry/Entity Type

Information Technology

Contact Information for Business Card

Denise Harlow Trumbey
482 West Maple Ridge Dr.
Brennick Falls, CO 76185

```html
<!DOCTYPE html>
<html lang="en">
<head>
<meta charset="utf-8">
<title>Vantrell Advisory — Business Card</title>
<link rel="stylesheet" href="https://fonts.googleapis.com/css2?family=Arimo:wght@400;700&display=swap">
<style>
  :root {
    --backdrop: #5ecfbd;
    --card: #f4f4f1;
    --teal: #0e9283;
    --tan: #b3a68c;
    --ink: #2a2a2a;
  }
  html, body {
    margin: 0;
    padding: 0;
    width: 1200px;
    height: 1000px;
    overflow: hidden;
    background: var(--backdrop);
    font-family: "Arimo", Arial, sans-serif;
  }
  .canvas {
    position: relative;
    width: 1200px;
    height: 1000px;
  }
  .business-card {
    position: absolute;
    left: 250px;
    top: 290px;
    width: 700px;
    height: 400px;
    background: var(--card);
  }
  .corner-block {
    position: absolute;
    left: 0;
    top: 0;
    width: 150px;
    height: 130px;
    background: var(--teal);
  }
  .brand-name {
    position: absolute;
    left: 40px;
    top: 175px;
    margin: 0;
    color: var(--teal);
    font-size: 30px;
    font-weight: 400;
    line-height: 1.1;
  }
  .holder-name {
    position: absolute;
    left: 300px;
    top: 48px;
    margin: 0;
    color: var(--ink);
    font-size: 22px;
    font-weight: 400;
  }
  .contact {
    position: absolute;
    left: 300px;
    top: 100px;
    margin: 0;
    color: var(--ink);
    font-size: 17px;
    line-height: 1.45;
    font-style: normal;
  }
  .contact .label { color: var(--teal); margin-right: 4px; }
  .contact .gap { display: block; height: 12px; }
  .stripe-block {
    position: absolute;
    left: 300px;
    top: 250px;
    width: 320px;
    height: 120px;
  }
</style>
</head>
<body>
  <main class="canvas">
    <section class="business-card" aria-label="Business card">
      <div class="corner-block"></div>
      <h1 class="brand-name">Vantrell<br>Advisory</h1>
      <h2 class="holder-name">Denise Harlow Trumbey</h2>
      <address class="contact">
        <span class="label">T.</span>555-204-0148<br>
        <span class="label">e.</span>d.trumbey@vantrelladvisory.com
        <span class="gap"></span>
        482 West Maple Ridge Dr.<br>
        Brennick Falls, CO 76185
      </address>
      <svg class="stripe-block" viewBox="0 0 320 120" aria-hidden="true">
        <rect x="0" y="0" width="320" height="44" fill="var(--teal)"/>
        <rect x="0" y="44" width="320" height="30" fill="var(--tan)"/>
        <rect x="0" y="74" width="320" height="46" fill="var(--teal)"/>
      </svg>
    </section>
  </main>
</body>
</html>
```